Data company needs a Website designed, coded and published.

We are a startup data company that needs to build a professional website.
Our business, Marrowby Reach, provides PII data to large national advertisers so they can precisely target Real People who are their consumers with advertising messages.

As a startup in this space, our website must establish our credibility and position us against significantly larger and more established competitors. Because we are in a data and technology space, it is vital for this slight to be incredibly slick and professional. Additionally, the purpose of the site is to inform potential customers about the quality of our data, the safety and security measures we take, should provide insight on how a prospect could engage us and ultimately the site should capture potential leads for us.

We have provided the attached presentation deck that is intended to give you an idea of the kind of content we'd like to have on the site. This deck is not intended to restrict your creativity in how the site should look and what it should say. It's simply intended to give you an outline of what we want to say.

We are open to your creative and alternative approaches.

Industry/Entity Type

Technology, Data, Media

Coding

Coded - Design and coding required

Number of Pages Required

5+ page

Font styles to use
Sans Serif

Colors

Designer to choose colors to be used in the design.

Requirements
Must have
• Professional looking site that positions us among the very best in our industry.
Nice to have
• We are about targeting real people with media and so we want to have good clean images of REAL People throughout the site.

```html
<!DOCTYPE html>
<html lang="en">
<head>
<meta charset="utf-8">
<title>Marrowby Reach — PII Data for Precise Targeting</title>
<link rel="stylesheet" href="https://fonts.googleapis.com/css2?family=Poppins:ital,wght@0,400;0,500;0,600;0,700;1,400&display=swap">
<style>
:root{
  --blue:#1565e0;
  --blue-bright:#1e8ff0;
  --cyan:#20b8f5;
  --ink:#141414;
  --text:#333a44;
  --muted:#6b7280;
  --card:#f0f1f3;
  --soft:#eef0f3;
  --dark:#232427;
  --darker:#1b1c1f;
  --white:#ffffff;
}
*{box-sizing:border-box;margin:0;padding:0}
html,body{width:1200px;height:5034px;overflow:hidden}
body{font-family:"Poppins",sans-serif;color:var(--text);background:var(--white);position:relative}
section,header,footer{position:relative;width:1200px;overflow:hidden}
.abs{position:absolute}
.btn{position:absolute;display:flex;align-items:center;justify-content:center;color:var(--white);font-weight:600;font-size:20px;background:linear-gradient(90deg,var(--cyan),var(--blue-bright));border-radius:2px}
.check{display:inline-block;width:18px;height:14px;flex:none}

/* header */
.site-header{height:137px;background:var(--white)}
.brand{position:absolute;left:74px;top:52px;display:flex;align-items:center;gap:8px;font-weight:700;font-size:23px;line-height:32px;color:var(--ink);white-space:nowrap}
.brand-dot{width:14px;height:14px;border-radius:50%;background:var(--blue);flex:none}
.nav{position:absolute;left:336px;top:58px;display:flex;gap:40px;font-size:16px;font-weight:600;color:var(--ink);white-space:nowrap}

/* hero */
.hero{height:680px;background:linear-gradient(100deg,#3c4048 0%,#6a6c70 45%,#4a4d52 100%)}
.hero-photo{position:absolute;inset:0;background:linear-gradient(100deg,rgba(40,44,52,.85) 0%,rgba(90,92,96,.4) 55%,rgba(60,58,56,.2) 100%),linear-gradient(160deg,#8a8c8e,#3a3d42)}
.hero h1{position:absolute;left:74px;top:182px;font-size:60px;line-height:60px;font-weight:700;color:var(--white)}
.hero p{position:absolute;left:74px;top:330px;font-size:20px;line-height:34px;color:var(--white);font-weight:500}
.dots{position:absolute;left:74px;top:600px;display:flex;gap:8px}
.dots span{width:13px;height:13px;border-radius:3px;background:var(--white)}
.dots span:first-child{background:var(--blue-bright)}

/* headings */
.sec-title{position:absolute;left:0;width:1200px;text-align:center;font-weight:700;font-size:48px;color:var(--ink)}

/* solutions */
.solutions{height:1063px}
.sol-sub{position:absolute;left:0;width:1200px;top:190px;text-align:center;font-size:34px;font-weight:600;color:var(--blue)}
.step{position:absolute;top:283px;width:329px;height:590px;background:var(--card);border-radius:165px 165px 28px 28px;padding:0 28px}
.step-icon{position:absolute;left:96px;top:28px;width:136px;height:136px;border-radius:50%;background:linear-gradient(135deg,var(--blue-bright),var(--blue));display:flex;align-items:center;justify-content:center}
.step h3{position:absolute;left:0;right:0;top:188px;text-align:center;font-size:28px;font-weight:600;color:var(--ink)}
.step-body{position:absolute;left:28px;right:24px;top:252px;font-size:14px;line-height:26px}
.step-body h4{color:var(--blue);font-size:17px;font-weight:600;margin-top:10px}
.step-body h4:first-child{margin-top:0}
.grid2{display:grid;grid-template-columns:1fr 1fr;row-gap:16px;margin-top:16px;color:var(--blue);font-size:16px}
.grid2 li,.ticks li{list-style:none;display:flex;align-items:center;gap:12px}
.ticks{margin:4px 0 6px}
.ticks li{line-height:30px}

/* services */
.services{height:754px;background:linear-gradient(110deg,#1a6be6 0%,#1c8aef 55%,#2ab5f6 100%)}
.tabs{position:absolute;top:213px;left:400px;display:flex;gap:36px;font-size:19px;color:var(--white)}
.tab{padding:6px 18px;border:2px solid transparent}
.tab.active{border-color:var(--white)}
.svc{position:absolute;top:320px;width:329px;height:346px;background:var(--white);border-radius:20px;text-align:center;padding:0 30px}
.svc svg{margin-top:36px}
.svc h3{font-size:23px;line-height:30px;font-weight:600;color:var(--blue);margin-top:10px}
.svc p{font-size:14px;line-height:26px;color:var(--text);margin-top:6px}
.svc p.note{font-style:italic;color:var(--blue);margin-top:0}

/* about */
.about{height:633px}
.frame-back{position:absolute;left:59px;top:59px;width:525px;height:480px;background:var(--cyan);border-radius:30px}
.photo{position:absolute;border-radius:26px}
.dot-grid{position:absolute;background-image:radial-gradient(var(--ink) 2px,transparent 2.5px);background-size:20px 20px}
.about h2,.why h2{position:absolute;font-size:46px;font-weight:700;color:var(--ink)}
.copy{position:absolute;font-size:15px;line-height:28px;text-align:center;color:var(--text)}
.deco{position:absolute;border-radius:50%;background:radial-gradient(ellipse,#4b78a8 0%,rgba(120,160,200,.35) 55%,transparent 72%)}

/* why */
.why{height:618px;background:var(--soft)}

/* contact */
.contact{height:738px}
.contact h3{position:absolute;left:74px;top:262px;font-size:30px;font-weight:600;color:var(--blue)}
.contact .lead{position:absolute;left:74px;top:312px;font-size:16px}
.benefits{position:absolute;left:74px;top:352px;font-size:16px;color:var(--ink)}
.benefits li{list-style:none;display:flex;align-items:center;gap:16px;height:47px}
.benefits b{color:var(--blue);font-weight:600}
.form-panel{position:absolute;left:614px;top:210px;width:514px;height:462px;background:linear-gradient(135deg,var(--blue-bright),var(--blue));border-radius:40px 20px 20px 20px}
.form-panel h3{position:absolute;left:29px;top:22px;color:var(--white);font-size:30px;line-height:42px;font-weight:600}
.field{position:absolute;left:29px;width:453px;height:50px;background:var(--white);font-size:14px;color:var(--ink);display:flex;align-items:center;padding-left:14px}
.submit{position:absolute;left:29px;top:390px;width:453px;height:49px;background:var(--ink);color:var(--white);font-weight:600;font-size:19px;display:flex;align-items:center;justify-content:center}

/* footer */
.site-footer{height:337px;background:var(--dark);color:#cfd2d6}
.foot-brand{position:absolute;left:74px;top:150px;display:flex;align-items:center;gap:8px;font-size:26px;font-weight:700;color:var(--white);white-space:nowrap}
.foot-col{position:absolute;top:62px;font-size:14px;line-height:35px}
.foot-col h4{font-size:18px;color:var(--white);font-weight:600;line-height:34px;margin-bottom:2px}
.foot-col li{list-style:none}
.bottom-bar{height:74px;background:var(--darker);color:#c9ccd0;font-size:14px}
.bottom-bar .copyright{position:absolute;left:74px;top:26px}
.socials{position:absolute;right:72px;top:24px;display:flex;gap:22px}
.socials span{width:24px;height:24px;border-radius:50%;background:var(--white)}
</style>
</head>
<body>

<header class="site-header">
  <div class="brand"><span class="brand-dot"></span>Marrowby Reach</div>
  <nav class="nav"><span>Our Data</span><span>Solutions</span><span>About Us</span><span>Why the Dragonfly?</span><span>Careers</span><span>Contact Us</span></nav>
</header>

<section class="hero">
  <div class="hero-photo" role="img" aria-label="Smiling man with glasses and beard working at a laptop in an office"></div>
  <h1>PII Data for<br>Precise Targeting</h1>
  <p>Ethically and intelligently target REAL PEOPLE with your<br>programmatic media. No Cookies. No Bots.</p>
  <a class="btn" style="left:74px;top:428px;width:204px;height:57px">Learn More</a>
  <div class="dots"><span></span><span></span><span></span><span></span></div>
</section>

<section class="solutions">
  <div class="deco" style="left:0;top:70px;width:270px;height:150px" role="img" aria-label="Blue dragonfly illustration"></div>
  <div class="deco" style="left:1075px;top:220px;width:150px;height:110px" role="img" aria-label="Dragonfly illustration"></div>
  <h2 class="sec-title" style="top:96px">Solutions</h2>
  <div class="sol-sub">Three Steps to Drive Results</div>

  <article class="step" style="left:74px">
    <div class="step-icon"><svg width="70" height="70" viewBox="0 0 70 70" fill="none" stroke="#fff" stroke-width="3"><circle cx="35" cy="20" r="7"/><path d="M24 40a11 11 0 0 1 22 0"/><circle cx="20" cy="45" r="6"/><circle cx="50" cy="45" r="6"/><path d="M8 64a12 12 0 0 1 24 0M38 64a12 12 0 0 1 24 0"/></svg></div>
    <h3>1. Audience</h3>
    <div class="step-body">
      <h4>Look A Like</h4><p>Use customer data to find the Real People most likely to buy.</p>
      <h4>Pre Built</h4><p>Pick from over 500 pre-built audiences of Real People</p>
      <h4>Custom Use the</h4><p>Use the 1000+ attributes to build a custom segment of Real People</p>
    </div>
  </article>

  <article class="step" style="left:434px">
    <div class="step-icon"><svg width="70" height="70" viewBox="0 0 70 70" fill="none" stroke="#fff" stroke-width="3"><rect x="24" y="8" width="22" height="22" rx="4"/><path d="M35 30v12M30 42v-8a4 4 0 0 1 8 0v8h8a5 5 0 0 1 5 5v9H26l-6-10"/><circle cx="12" cy="18" r="3"/><circle cx="58" cy="18" r="3"/><path d="M15 18h9M46 18h9"/></svg></div>
    <h3>2. Activation</h3>
    <div class="step-body">
      <p>Activate your defined audience of Real People across the media they use:</p>
      <ul class="grid2">
        <li><svg class="check" viewBox="0 0 18 14"><path d="M2 7l5 5 9-10" stroke="#1e8ff0" stroke-width="2.5" fill="none"/></svg>Email</li>
        <li><svg class="check" viewBox="0 0 18 14"><path d="M2 7l5 5 9-10" stroke="#1e8ff0" stroke-width="2.5" fill="none"/></svg>Audio</li>
        <li><svg class="check" viewBox="0 0 18 14"><path d="M2 7l5 5 9-10" stroke="#1e8ff0" stroke-width="2.5" fill="none"/></svg>Display</li>
        <li><svg class="check" viewBox="0 0 18 14"><path d="M2 7l5 5 9-10" stroke="#1e8ff0" stroke-width="2.5" fill="none"/></svg>Video</li>
        <li><svg class="check" viewBox="0 0 18 14"><path d="M2 7l5 5 9-10" stroke="#1e8ff0" stroke-width="2.5" fill="none"/></svg>Mobile</li>
        <li><svg class="check" viewBox="0 0 18 14"><path d="M2 7l5 5 9-10" stroke="#1e8ff0" stroke-width="2.5" fill="none"/></svg>Social</li>
        <li><svg class="check" viewBox="0 0 18 14"><path d="M2 7l5 5 9-10" stroke="#1e8ff0" stroke-width="2.5" fill="none"/></svg>Native</li>
        <li><svg class="check" viewBox="0 0 18 14"><path d="M2 7l5 5 9-10" stroke="#1e8ff0" stroke-width="2.5" fill="none"/></svg>Direct Mail</li>
      </ul>
    </div>
  </article>

  <article class="step" style="left:799px">
    <div class="step-icon"><svg width="70" height="70" viewBox="0 0 70 70" fill="none" stroke="#fff" stroke-width="3"><rect x="26" y="6" width="34" height="44" rx="3"/><path d="M33 16h20M33 25h20M33 34h12"/><path d="M14 40l6-8 6 8v22H14z"/><circle cx="52" cy="54" r="8"/></svg></div>
    <h3>3. Attribution</h3>
    <div class="step-body">
      <h4>You will know:</h4>
      <ul class="ticks">
        <li><svg class="check" viewBox="0 0 18 14"><path d="M2 7l5 5 9-10" stroke="#1e8ff0" stroke-width="2.5" fill="none"/></svg>Who was served your ad</li>
        <li><svg class="check" viewBox="0 0 18 14"><path d="M2 7l5 5 9-10" stroke="#1e8ff0" stroke-width="2.5" fill="none"/></svg>What devices they saw it on</li>
        <li><svg class="check" viewBox="0 0 18 14"><path d="M2 7l5 5 9-10" stroke="#1e8ff0" stroke-width="2.5" fill="none"/></svg>Who engaged</li>
        <li><svg class="check" viewBox="0 0 18 14"><path d="M2 7l5 5 9-10" stroke="#1e8ff0" stroke-width="2.5" fill="none"/></svg>Who bought</li>
        <li><svg class="check" viewBox="0 0 18 14"><path d="M2 7l5 5 9-10" stroke="#1e8ff0" stroke-width="2.5" fill="none"/></svg>Who visited your store</li>
        <li><svg class="check" viewBox="0 0 18 14"><path d="M2 7l5 5 9-10" stroke="#1e8ff0" stroke-width="2.5" fill="none"/></svg>...Each down to the person.</li>
      </ul>
      <p>Answering the most important question:</p>
      <p>Who should we target next?</p>
    </div>
  </article>

  <a class="btn" style="left:457px;top:924px;width:286px;height:59px">Schedule a Demo</a>
</section>

<section class="services">
  <h2 class="sec-title" style="top:100px;color:var(--white)">Our Services</h2>
  <div class="tabs"><span class="tab active">Managed Services</span><span class="tab">Data Services</span></div>

  <article class="svc" style="left:74px">
    <svg width="100" height="100" viewBox="0 0 100 100" fill="none" stroke="#1e8ff0" stroke-width="3"><circle cx="50" cy="50" r="44"/><circle cx="50" cy="50" r="30"/><path d="M50 2v16M50 82v16M2 50h16M82 50h16"/><circle cx="50" cy="44" r="6"/><path d="M38 62a12 12 0 0 1 24 0"/></svg>
    <h3>Audience<br>Identification</h3>
    <p>Real People target audience and segmentation Matching Customer file to MRD Database.</p>
  </article>
  <article class="svc" style="left:434px">
    <svg width="100" height="100" viewBox="0 0 100 100" fill="none" stroke="#1e8ff0" stroke-width="3"><path d="M36 26a14 14 0 1 1 22 0"/><path d="M42 56V24a5 5 0 0 1 10 0v26l18 4a7 7 0 0 1 6 8l-3 26H44L28 66a5 5 0 0 1 8-6z"/></svg>
    <h3>Activation</h3>
    <p>Account Management Planning and Activation</p>
    <p class="note">(Email, Display, Streaming Audio, Streaming Video, OTT and Social Media)</p>
  </article>
  <article class="svc" style="left:799px">
    <svg width="100" height="100" viewBox="0 0 100 100" fill="none" stroke="#1e8ff0" stroke-width="3"><path d="M20 6h46l14 14v74H20z"/><rect x="30" y="18" width="36" height="14"/><path d="M30 46l5 5 8-9M50 48h22M30 66l5 5 8-9M50 68h14"/><path d="M74 60l16-16 6 6-16 16-8 2z"/></svg>
    <h3>Results</h3>
    <p>Audience Insights and Recommendations POS Matchback Closed Loop Attribution and Reporting</p>
  </article>
</section>

<section class="about">
  <div class="frame-back"></div>
  <div class="photo" style="left:72px;top:72px;width:514px;height:458px;background:linear-gradient(135deg,#5b6068,#a9aeb4 55%,#d5d2cc)" role="img" aria-label="Two colleagues reviewing a tablet beside server racks in a data centre"></div>
  <div class="dot-grid" style="left:468px;top:430px;width:150px;height:180px"></div>
  <h2 style="left:666px;top:120px">About Company</h2>
  <div class="copy" style="left:614px;top:238px;width:512px">After building four successful marketing companies (Unified Media Works, Signal Inc, Reachline Direct and Northgate Trading) each acquired by public companies (Halvern Group and Corbet Partners), Dale Preston is back with a revolutionary new approach to programmatic media.<br>Marrowby Reach offers PII Data so marketers can target real people in an intelligent and ethical way - and respecting individuals privacy.</div>
  <a class="btn" style="left:762px;top:487px;width:211px;height:57px">Read More</a>
  <div class="deco" style="left:990px;top:450px;width:210px;height:160px" role="img" aria-label="Dragonfly illustration"></div>
</section>

<section class="why">
  <div class="abs" style="left:640px;top:60px;width:500px;height:420px;background:var(--cyan);border-radius:30px"></div>
  <div class="photo" style="left:614px;top:78px;width:514px;height:465px;background:linear-gradient(150deg,#cfe4d4 0%,#8fc08a 45%,#3f7f4a 100%)" role="img" aria-label="Blue dragonfly resting on a green leaf"></div>
  <div class="dot-grid" style="left:574px;top:420px;width:70px;height:160px"></div>
  <h2 style="left:86px;top:124px">Why the Dragonfly?</h2>
  <div class="copy" style="left:86px;top:238px;width:480px">Which animal is the most accurate and precise hunter in the animal kingdom?<br>The Lion, the Tiger, The Great White Shark…<br>Nope…It's the Dragonfly!<br>95% of the time the Dragonfly hunts it catches its prey!<br>We named our company Marrowby Reach because we believe with our data marketers can be just as precise and accurate!</div>
  <a class="btn" style="left:221px;top:485px;width:211px;height:58px">Read More</a>
</section>

<section class="contact">
  <div class="deco" style="left:0;top:10px;width:270px;height:170px" role="img" aria-label="Blue dragonfly illustration"></div>
  <h2 class="sec-title" style="top:118px">Contact Us</h2>
  <div class="dot-grid" style="left:1010px;top:170px;width:150px;height:80px"></div>
  <div class="dot-grid" style="left:574px;top:570px;width:150px;height:150px"></div>
  <h3>Ready to Learn More?</h3>
  <p class="lead">Talk to our experts now.</p>
  <ul class="benefits">
    <li><svg class="check" viewBox="0 0 18 14"><path d="M2 7l5 5 9-10" stroke="#1e8ff0" stroke-width="2.5" fill="none"/></svg>We'll find a solution that's right for your business.</li>
    <li><svg class="check" viewBox="0 0 18 14"><path d="M2 7l5 5 9-10" stroke="#1e8ff0" stroke-width="2.5" fill="none"/></svg>Reach more potential customers</li>
    <li><svg class="check" viewBox="0 0 18 14"><path d="M2 7l5 5 9-10" stroke="#1e8ff0" stroke-width="2.5" fill="none"/></svg>Gain control of your reach and frequency</li>
    <li><svg class="check" viewBox="0 0 18 14"><path d="M2 7l5 5 9-10" stroke="#1e8ff0" stroke-width="2.5" fill="none"/></svg>Reduce wasteful spending on bad targeting</li>
    <li><svg class="check" viewBox="0 0 18 14"><path d="M2 7l5 5 9-10" stroke="#1e8ff0" stroke-width="2.5" fill="none"/></svg><span>Connect with our database of <b>160M Real People</b></span></li>
    <li><svg class="check" viewBox="0 0 18 14"><path d="M2 7l5 5 9-10" stroke="#1e8ff0" stroke-width="2.5" fill="none"/></svg><span>Build your <b>Post Cookie Growth Plan</b></span></li>
  </ul>
  <form class="form-panel">
    <h3>We're happy to answer<br>your questions.</h3>
    <div class="field" style="top:132px">Name</div>
    <div class="field" style="top:196px;width:218px">Title</div>
    <div class="field" style="top:196px;left:264px;width:218px">Company</div>
    <div class="field" style="top:259px">Email Address</div>
    <div class="field" style="top:323px">Anything Else You'd Like to Share</div>
    <div class="submit">Get In Touch</div>
  </form>
</section>

<footer class="site-footer">
  <div class="foot-brand"><span class="brand-dot"></span>Marrowby Reach</div>
  <div class="foot-col" style="left:358px"><h4>Site Map</h4><ul><li>Our Data</li><li>Solutions</li><li>About Us</li><li>Why the Dragonfly?</li><li>Careers</li><li>Contact Us</li></ul></div>
  <div class="foot-col" style="left:627px"><h4>Support</h4><ul><li>Sed ut perspiciatis</li><li>Unde omnis iste</li><li>Natus error sit volup</li><li>Tatem accusantium</li><li>Doloremque</li></ul></div>
  <div class="foot-col" style="left:903px"><h4>Resources</h4><ul><li>Sed ut perspiciatis</li><li>Unde omnis iste</li><li>Natus error sit volup</li><li>Tatem accusantium</li><li>Doloremque</li></ul></div>
</footer>
<footer class="bottom-bar">
  <span class="copyright">Copyright © 2023 CompanyName. All Right Reserved</span>
  <div class="socials" aria-label="Social links"><span></span><span></span><span></span><span></span><span></span></div>
</footer>

</body>
</html>
```